Business card for Luxury Portable Restroom Trailer company

We are a Luxury Portable Restroom Trailer Company Called PELIKAR HIRES. Based in Orange County California. We provide portable restroom trailers for events, such as, Weddings, Concerts, Charity events, Sporting events, Tournaments, Corporate events, ect. We rent and Sell the Luxury restrooms. Our colors are white, grey, and Orange. As you will see in the logo we uploaded.
There are 2 people in the company so the names and titles will change for the 3 people but card will remain the same. Here is the information for each Person: Dennis Moyle CFO 555 018-3647
next Person: Wesley Tanford VP 555 018-3647
Next Person: Miles Tanford CEO 555 018-3647
Information to include on the card: Luxury Restroom Trailers Rental and Sales. Weddings, Concerts, Charity, Sporting and Corp. Events.

```html
<!DOCTYPE html>
<html lang="en">
<head>
<meta charset="utf-8">
<title>Pelikar Hires – Business Card</title>
<link rel="stylesheet" href="https://fonts.googleapis.com/css2?family=Montserrat:wght@800&family=Open+Sans:wght@400;700&family=Quicksand:wght@500&display=swap">
<style>
  :root {
    --backdrop: #9b9b9b;
    --card: #ffffff;
    --orange: #f26b21;
    --grey: #4a4a4a;
    --white: #ffffff;
  }
  * { margin: 0; padding: 0; box-sizing: border-box; }
  html, body { width: 1200px; height: 822px; overflow: hidden; }
  body {
    background: var(--backdrop);
    position: relative;
    font-family: "Quicksand", sans-serif;
  }
  .card {
    position: absolute;
    top: 289px;
    width: 388px;
    height: 251px;
    background: var(--card);
    overflow: hidden;
  }
  .card--front { left: 164px; }
  .card--back { left: 640px; }

  .wordmark {
    position: absolute;
    left: 0; right: 0;
    text-align: center;
    font-family: "Montserrat", sans-serif;
    font-weight: 800;
    color: var(--orange);
    letter-spacing: 0.5px;
    white-space: nowrap;
  }
  .card--front .wordmark { top: 44px; font-size: 23px; }
  .card--back .wordmark { top: 108px; font-size: 27px; }

  .band {
    position: absolute;
    left: 0; right: 0;
    height: 44px;
    background: var(--orange);
    clip-path: polygon(1.7% 0, 98.3% 0, 100% 35%, 100% 100%, 0 100%, 0 35%);
  }
  .card--front .band { top: 114px; }
  .card--back .band { top: 207px; }

  .band__emblem {
    position: absolute;
    top: 2px;
    width: 52px;
    height: 42px;
    background: var(--white);
    border-radius: 0 0 40% 40%;
  }
  .band__emblem--left { left: 4px; }
  .band__emblem--right { right: 4px; }

  .person {
    position: absolute;
    top: 0; left: 0; right: 0;
    text-align: center;
    color: var(--white);
  }
  .person__name {
    font-family: "Open Sans", sans-serif;
    font-weight: 700;
    font-size: 19px;
    line-height: 1;
    margin-top: 6px;
    letter-spacing: 0.3px;
  }
  .person__title {
    font-family: "Quicksand", sans-serif;
    font-size: 12px;
    line-height: 1;
    margin-top: 4px;
  }

  .details {
    position: absolute;
    top: 176px;
    left: 0; right: 0;
    text-align: center;
    color: var(--grey);
    font-size: 12.5px;
    line-height: 17.5px;
    white-space: nowrap;
  }
  .details__services { color: var(--orange); }
  .details__sep { color: var(--grey); }
</style>
</head>
<body>
  <section class="card card--front">
    <div class="wordmark">PELIKAR HIRES</div>
    <div class="band">
      <div class="band__emblem band__emblem--left" role="img" aria-label="White animal head emblem"></div>
      <div class="person">
        <div class="person__name">DENNIS MOYLE</div>
        <div class="person__title">CFO</div>
      </div>
      <div class="band__emblem band__emblem--right" role="img" aria-label="White animal head emblem"></div>
    </div>
    <div class="details">
      <div class="details__phone">555 018-3647</div>
      <div class="details__tagline">Luxury Restroom Trailers Rental and Sales.</div>
      <div class="details__services">Weddings<span class="details__sep">, </span>Concerts<span class="details__sep">, </span>Charity<span class="details__sep">, </span>Sporting <span class="details__sep">&amp;</span> Corp<span class="details__sep">, </span>Events.</div>
    </div>
  </section>

  <section class="card card--back">
    <div class="wordmark">PELIKAR HIRES</div>
    <div class="band">
      <div class="band__emblem band__emblem--left" role="img" aria-label="White animal head emblem"></div>
      <div class="band__emblem band__emblem--right" role="img" aria-label="White animal head emblem"></div>
    </div>
  </section>
</body>
</html>
```